KVT Roofing Pty Ltd

We are a high end residential Roofing company
We would like something silimar to the attached logo with the same color scheme

Target Market(s)

High end residential Builders & Architects

Industry/Entity Type

Residential

```html
<!DOCTYPE html>
<html lang="en">
<head>
<meta charset="utf-8">
<title>KVT Roofing Pty Ltd – Business Card</title>
<link rel="stylesheet" href="https://fonts.googleapis.com/css2?family=Open+Sans:wght@400;600;700;800&display=swap">
<style>
  :root {
    --backdrop: #7d4330;
    --card-white: #ffffff;
    --slate: #4a5964;
    --roof-blue: #0399c8;
    --text-light: #ffffff;
  }
  * { margin: 0; padding: 0; box-sizing: border-box; }
  html, body {
    width: 1200px; height: 900px; overflow: hidden;
    background: var(--backdrop);
    font-family: "Open Sans", Arial, sans-serif;
  }
  .canvas { position: relative; width: 1200px; height: 900px; }

  /* Front of card */
  .card-front {
    position: absolute; left: 226px; top: 217px;
    width: 445px; height: 255px;
    background: var(--card-white);
    border-radius: 30px 30px 0 0;
    overflow: hidden;
  }
  .card-front .brand-name {
    position: absolute; left: 0; right: 0; top: 130px;
    text-align: center;
    font-weight: 800; font-size: 27px; letter-spacing: 0.5px;
    color: var(--slate);
    display: flex; align-items: center; justify-content: center; gap: 10px;
  }
  .brand-square { width: 18px; height: 18px; background: var(--roof-blue); display: inline-block; }
  .card-front .accent-line {
    position: absolute; left: 0; right: 0; top: 220px; height: 3px;
    background: var(--roof-blue);
  }
  .card-front .base-band {
    position: absolute; left: 0; right: 0; top: 226px; bottom: 0;
    background: var(--slate);
  }

  /* Back of card */
  .card-back {
    position: absolute; left: 530px; top: 426px;
    width: 445px; height: 256px;
    border-radius: 0 30px 0 0;
    overflow: hidden;
    display: flex;
  }
  .card-back .brand-panel {
    width: 164px; background: var(--slate);
    display: flex; align-items: center; justify-content: center;
  }
  .card-back .brand-panel .brand-name {
    color: var(--text-light); font-weight: 700; font-size: 12.5px;
    text-align: center; line-height: 1.25; margin-top: 10px;
  }
  .card-back .details-panel {
    flex: 1; background: var(--roof-blue); color: var(--text-light);
    position: relative;
  }
  .person-name { position: absolute; left: 18px; top: 40px; font-size: 13px; font-weight: 600; letter-spacing: 0.3px; }
  .person-role { position: absolute; left: 18px; top: 58px; font-size: 13px; font-weight: 600; }
  .contact-list { position: absolute; left: 18px; top: 176px; list-style: none; }
  .contact-list li {
    display: flex; align-items: center; gap: 4px;
    font-size: 12px; font-weight: 600; height: 16px; margin-bottom: 8px;
  }
  .contact-icon { width: 14px; height: 14px; flex: none; }
</style>
</head>
<body>
<div class="canvas">

  <section class="card-front">
    <div class="brand-name"><span class="brand-square"></span>KVT ROOFING PTY LTD</div>
    <div class="accent-line"></div>
    <div class="base-band"></div>
  </section>

  <section class="card-back">
    <div class="brand-panel">
      <div class="brand-name">KVT ROOFING<br>PTY LTD</div>
    </div>
    <div class="details-panel">
      <p class="person-name">CORRAN WHITFIELD</p>
      <p class="person-role">General Manager</p>
      <ul class="contact-list">
        <li>
          <svg class="contact-icon" viewBox="0 0 14 14" aria-hidden="true">
            <rect width="14" height="14" rx="3" fill="#fff"/>
            <path d="M7 2.5a3 3 0 0 0-3 3c0 2.2 3 5.8 3 5.8s3-3.6 3-5.8a3 3 0 0 0-3-3z" fill="none" stroke="#0399c8" stroke-width="1.2"/>
          </svg>
          212 Larkin Street, Port Ellery
        </li>
        <li>
          <svg class="contact-icon" viewBox="0 0 14 14" aria-hidden="true">
            <rect width="14" height="14" rx="3" fill="#fff"/>
            <path d="M4.5 3h2l.6 2-1.2.9a6 6 0 0 0 2.2 2.2l.9-1.2 2 .6v2c0 .5-.4.9-.9.9A6.6 6.6 0 0 1 3.6 3.9c0-.5.4-.9.9-.9z" fill="#0399c8"/>
          </svg>
          0400 118 265
        </li>
        <li>
          <svg class="contact-icon" viewBox="0 0 14 14" aria-hidden="true">
            <rect width="14" height="14" rx="3" fill="#fff"/>
            <rect x="2.8" y="4" width="8.4" height="6" fill="none" stroke="#0399c8" stroke-width="1.1"/>
            <path d="M2.8 4 7 7.5 11.2 4" fill="none" stroke="#0399c8" stroke-width="1.1"/>
          </svg>
          cwhitfield@kvtroofing.com.au
        </li>
      </ul>
    </div>
  </section>

</div>
</body>
</html>
```